A Maple Syrup Label for a Local Buniness

We are looking for a label for our maple syrup business. Our business currently sells honey, and we are expanding into maple syrup. Our Business name is "Brackley Honey" and we currently have a logo attached below. We would like to incorporate the bee and BH part, but the label could also read "Brackley Farms" with the words maple syrup. We do not want consumers to confuse the maple syrup jars with the honey jars. It should be clear that the jars contain maple syrup. We are open to new designs as well.

```html
<!DOCTYPE html>
<html lang="en">
<head>
<meta charset="utf-8">
<title>Brackley Farm Maple Syrup Label</title>
<link rel="stylesheet" href="https://fonts.googleapis.com/css2?family=Alegreya:wght@400;700;800&display=swap">
<style>
  :root {
    --backdrop: #0b0b0b;
    --paper: #ffffff;
    --ink: #2a2424;
    --gold: #f7c21b;
    --caption: #ffffff;
  }
  * { margin: 0; padding: 0; box-sizing: border-box; }
  html, body { width: 1200px; height: 945px; overflow: hidden; background: var(--backdrop); }
  .canvas { position: relative; width: 1200px; height: 945px; background: var(--backdrop); }

  .label {
    position: absolute; top: 112px; width: 485px; height: 721px;
    background: var(--paper); color: var(--ink);
    font-family: "Alegreya", Georgia, serif;
  }
  .label--front { left: 100px; }
  .label--back { left: 615px; }

  .flourish {
    position: absolute; width: 97px; height: 86px;
    background: radial-gradient(ellipse at var(--origin), rgba(247,194,27,0.55) 0%, rgba(247,194,27,0.25) 45%, rgba(247,194,27,0) 75%);
  }
  .flourish--tl { left: 39px; top: 39px; --origin: 0% 0%; }
  .flourish--tr { right: 36px; top: 39px; --origin: 100% 0%; }
  .flourish--bl { left: 39px; bottom: 40px; --origin: 0% 100%; }
  .flourish--br { right: 36px; bottom: 40px; --origin: 100% 100%; }

  .brand-title { position: absolute; left: 0; top: 78px; width: 485px; height: 130px; }
  .brand-title text { font-family: "Alegreya", Georgia, serif; font-weight: 800; fill: var(--ink); }

  .farm-illustration {
    position: absolute; left: 124px; top: 220px; width: 237px; height: 280px;
    border-radius: 48% 48% 50% 50% / 40% 40% 60% 60%;
    background: radial-gradient(ellipse at 50% 65%, #8a8585 0%, #4d4747 55%, #2e2929 100%);
  }

  .product-name {
    position: absolute; left: 0; top: 520px; width: 485px; text-align: center;
    font-weight: 800; font-size: 46px; letter-spacing: 0.5px; line-height: 1;
  }
  .net-volume {
    position: absolute; left: 0; top: 604px; width: 485px; text-align: center;
    font-weight: 700; font-size: 33px; letter-spacing: 0.5px; line-height: 1;
  }

  .story-heading {
    position: absolute; left: 70px; top: 145px; white-space: nowrap;
    font-weight: 700; font-size: 24px; line-height: 1;
  }
  .story-body {
    position: absolute; left: 70px; top: 202px; white-space: nowrap;
    font-size: 24px; line-height: 29.2px; letter-spacing: 0.3px;
  }
  .story-signoff {
    position: absolute; left: 70px; top: 468px; white-space: nowrap;
    font-weight: 700; font-size: 24px; line-height: 1;
  }

  .brand-mark {
    position: absolute; left: 142px; top: 568px; width: 200px; height: 30px;
    display: flex; align-items: center; justify-content: center; gap: 8px;
  }
  .brand-mark__dot { width: 14px; height: 14px; border-radius: 50%; background: var(--gold); flex: none; }
  .brand-mark__name { font-weight: 700; font-size: 22px; line-height: 1; color: var(--ink); white-space: nowrap; }

  .caption {
    position: absolute; top: 854px; width: 485px; text-align: center;
    font-family: Arial, Helvetica, sans-serif; font-size: 16px; color: var(--caption);
  }
  .caption--front { left: 100px; }
  .caption--back { left: 615px; }
</style>
</head>
<body>
<main class="canvas">
  <section class="label label--front">
    <div class="flourish flourish--tl" role="img" aria-label="Gold filigree corner ornament"></div>
    <div class="flourish flourish--tr" role="img" aria-label="Gold filigree corner ornament"></div>
    <div class="flourish flourish--bl" role="img" aria-label="Gold filigree corner ornament"></div>
    <div class="flourish flourish--br" role="img" aria-label="Gold filigree corner ornament"></div>

    <svg class="brand-title" viewBox="0 0 485 130" aria-label="Brackley Farm">
      <defs>
        <path id="title-arc" d="M 85 64 Q 242 34 400 64"/>
      </defs>
      <text font-size="62" text-anchor="middle">
        <textPath href="#title-arc" startOffset="50%" textLength="312" lengthAdjust="spacingAndGlyphs">BRACKLEY</textPath>
      </text>
      <text x="242" y="116" font-size="62" text-anchor="middle" letter-spacing="1">FARM</text>
    </svg>

    <div class="farm-illustration" role="img" aria-label="Engraved illustration of a bee hovering above an oval vignette of a barn, tree and fence"></div>

    <h1 class="product-name">MAPLE SYRUP</h1>
    <p class="net-volume">12 FL OZ</p>
  </section>

  <section class="label label--back">
    <div class="flourish flourish--tl" role="img" aria-label="Gold filigree corner ornament"></div>
    <div class="flourish flourish--tr" role="img" aria-label="Gold filigree corner ornament"></div>
    <div class="flourish flourish--bl" role="img" aria-label="Gold filigree corner ornament"></div>
    <div class="flourish flourish--br" role="img" aria-label="Gold filigree corner ornament"></div>

    <h2 class="story-heading">From Tree to Table — With Love</h2>
    <p class="story-body">Tapped from the maples on our<br>Ontario farm, our pure maple<br>syrup is hand-crafted by the<br>Brackley family using time-<br>honored methods. Every bottle<br>supports sustainable practices<br>and generations of family<br>farming.</p>
    <p class="story-signoff">– Brackley Farms</p>

    <div class="brand-mark">
      <span class="brand-mark__dot"></span>
      <span class="brand-mark__name">Brackley Honey</span>
    </div>
  </section>

  <p class="caption caption--front">Maple Syrup Label Front-Side</p>
  <p class="caption caption--back">Maple Syrup Label Back-Side Text (Suggested)</p>
</main>
</body>
</html>
```